'WILD' eye catching Business Card Design / Logo for production company / TV host / adventurer

Hi there,

We are looking for a 'WILD' and exciting logo and double sided business card for our business "Red Kettle Studios".

Corwin Baxley is an international television host, adventurer, author and inspirational public speaker.

We want to project Corwin's talents onto his business card.

We are looking for a business card design that can carry over onto letter heads, emails etc. We want a design that is 'WILD', different and exciting.

Feel free to check out Corwin's web site: www.redkettlestudios.co.nz to get a better understanding what he is about.

Please feel free to go completely 'WILD' on this project as we want something different with lots of WOW factors.

Thank you so much and we look forward to your designs.

We have a feeling that there will be many more designs in the near future.

Best regards,

the production team

We have added another task to the list.

If the winning designer can also provide us with a matching letterhead and email signature based on the same style of design as the business card.

Target Market(s)

People with passion.

Industry/Entity Type

Business

Requirements
Must have
• Red Kettle Studios
Corwin Baxley
42 Fernhill Lane
Ashbury 7388
New Zealand

Phone +64-(0)3-5027 416
Cell +64-(0)274-861 052

email: redkettlenz@mailbox-example.nz
www.redkettlestuios.co.nz
Nice to have
• A feature made out of the name 'Red Kettle Studios'.

Corwin Baxley's name reasonably obvious.

All other details (except web site) can be quite small.

```html
<!DOCTYPE html>
<html lang="en">
<head>
<meta charset="utf-8">
<title>Corwin Baxley – Red Kettle Studios business card</title>
<link rel="stylesheet" href="https://fonts.googleapis.com/css2?family=Arimo:wght@700&family=Caladea:wght@700&display=swap">
<style>
  :root {
    --paper: #ffffff;
    --ink: #111111;
    --name-red: #d0102a;
    --name-red-light: #f0607a;
    --role-blue: #1d3f8a;
    --address-purple: #6a1fa6;
    --address-red: #c8102e;
    --phone-gold: #a08a1c;
    --web-purple: #5b1a9a;
    --cell-1: #c8102e;
    --cell-2: #2e8b3a;
    --cell-3: #6a1fa6;
    --cell-4: #1d5fb8;
    --cell-5: #b07a10;
  }
  * { margin: 0; padding: 0; box-sizing: border-box; }
  html, body { width: 1200px; height: 686px; overflow: hidden; background: var(--paper); }
  .card {
    position: relative;
    width: 1200px;
    height: 686px;
    background: var(--paper);
    font-family: "Arimo", Arial, sans-serif;
    font-weight: 700;
  }
  .brand {
    position: absolute;
    left: 40px;
    top: 170px;
    font-size: 44px;
    letter-spacing: 1px;
    color: var(--ink);
    text-transform: uppercase;
  }
  .identity {
    position: absolute;
    left: 700px;
    top: 165px;
  }
  .identity__name {
    font-size: 66px;
    line-height: 1;
    letter-spacing: 2px;
    word-spacing: 10px;
    background: linear-gradient(180deg, var(--name-red) 0%, var(--name-red) 55%, var(--name-red-light) 100%);
    -webkit-background-clip: text;
    background-clip: text;
    color: transparent;
  }
  .identity__roles {
    margin-top: 12px;
    font-size: 24px;
    line-height: 36px;
    color: var(--role-blue);
    text-align: right;
    width: 486px;
  }
  .identity__cell {
    margin-top: 2px;
    font-family: "Caladea", Cambria, serif;
    font-size: 38px;
    line-height: 44px;
    white-space: nowrap;
  }
  .c1 { color: var(--cell-1); }
  .c2 { color: var(--cell-2); }
  .c3 { color: var(--cell-3); }
  .c4 { color: var(--cell-4); }
  .c5 { color: var(--cell-5); }
  .contact {
    position: absolute;
    left: 73px;
    top: 440px;
    font-size: 24px;
    line-height: 34px;
    list-style: none;
  }
  .contact__address { color: var(--address-purple); }
  .contact__country { color: var(--address-red); }
  .contact__phone { color: var(--phone-gold); }
  .contact__email { color: var(--address-red); }
  .website {
    position: absolute;
    left: 73px;
    top: 622px;
    font-size: 34px;
    color: var(--web-purple);
  }
</style>
</head>
<body>
  <main class="card">
    <div class="brand">Red Kettle Studios</div>

    <section class="identity">
      <h1 class="identity__name">Corwin Baxley</h1>
      <p class="identity__roles">Television host , adventurer, author<br>and inspirational public speaker</p>
      <p class="identity__cell"><span class="c1">cell</span><span class="c3">:</span><span class="c4">64</span><span class="c1">-(</span><span class="c2">0</span><span class="c1">)</span><span class="c4">274</span><span class="c3">-</span><span class="c5">861</span> <span class="c2">0</span><span class="c3">5</span><span class="c1">2</span></p>
    </section>

    <ul class="contact">
      <li class="contact__address">42 Fernhill Lane</li>
      <li class="contact__address">Ashbury 7388</li>
      <li class="contact__country">New Zealand</li>
      <li class="contact__phone">phone: 64-(0)3-5027 416</li>
      <li class="contact__email">email: redkettlenz@mailbox-example.nz</li>
    </ul>

    <p class="website">www.redkettlestudios.co.nz</p>
  </main>
</body>
</html>
```